Tattoo Shop Business Card

I need a Business Card for the The Harbor Quill.

I'm thinking i want a double sided business card, really clean, very classy, one side the logo, and on the other my information. I'm pretty much open to anything, as long as its fun and captures class and elegance, while at the same time is edgy and tattooish.
I don't want your typical classic card. Add your own twist on it

Logo is attached to this brief

Please include:
Name
Position
Phone Number
Email
Website

Target Market(s)

I'm looking to capture potential clients for my tattoo shop so the card needs to be something they can fit in their wallet but they will also remember me when they see that card in there. My target audience is everyone over 18 that is intrigued by tattoos and piercings.

Industry/Entity Type

Business

Font styles to use
Serif

Colors

Designer to choose colors to be used in the design.

Requirements
Must have
• must be bold and something people will never forget

```html
<!DOCTYPE html>
<html lang="en">
<head>
<meta charset="utf-8">
<title>The Harbor Quill – Business Card</title>
<link href="https://fonts.googleapis.com/css2?family=Libre+Baskerville:ital,wght@0,400;0,700;1,700&display=swap" rel="stylesheet">
<style>
  :root {
    --stage: #000000;
    --paper: #ffffff;
    --ink: #141010;
    --name-ink: #2b120c;
    --name-edge: #c2361f;
    --position: #7d2519;
    --tile-phone: #7a2a22;
    --tile-mail: #e0532f;
    --tile-web: #9dab5a;
    --divider: #f2ece4;
    --warm-red: #e2392c;
    --warm-orange: #f08a32;
    --warm-yellow: #f6c64a;
    --warm-dark: #2a1714;
    --warm-green: #6f8f34;
  }
  * { margin: 0; padding: 0; box-sizing: border-box; }
  html, body { width: 1200px; height: 1200px; overflow: hidden; background: var(--stage); }
  .canvas { position: relative; width: 1200px; height: 1200px; font-family: "Libre Baskerville", Georgia, serif; }

  .card-front, .card-back-art, .card-back-info { position: absolute; overflow: hidden; }

  .card-front { left: 202px; top: 62px; width: 784px; height: 470px; }
  .prism-field { position: absolute; inset: 0; }
  .card-front .prism-field {
    background:
      radial-gradient(ellipse 45% 40% at 58% 52%, rgba(250,214,90,.95), rgba(250,214,90,0) 70%),
      radial-gradient(ellipse 30% 35% at 90% 70%, rgba(111,143,52,.85), rgba(111,143,52,0) 70%),
      radial-gradient(ellipse 35% 45% at 95% 15%, rgba(30,22,26,.95), rgba(30,22,26,0) 75%),
      radial-gradient(ellipse 30% 40% at 5% 20%, rgba(226,57,44,.95), rgba(226,57,44,0) 75%),
      radial-gradient(ellipse 25% 30% at 12% 70%, rgba(60,30,30,.7), rgba(60,30,30,0) 75%),
      linear-gradient(135deg, var(--warm-red), var(--warm-orange) 45%, #c94a38 100%);
  }

  .card-back-art { left: 200px; top: 565px; width: 384px; height: 480px; }
  .card-back-art .prism-field {
    background:
      radial-gradient(ellipse 55% 35% at 25% 60%, rgba(247,200,74,.95), rgba(247,200,74,0) 70%),
      radial-gradient(ellipse 35% 30% at 85% 20%, rgba(70,35,35,.75), rgba(70,35,35,0) 75%),
      radial-gradient(ellipse 40% 30% at 80% 90%, rgba(120,110,50,.6), rgba(120,110,50,0) 75%),
      linear-gradient(165deg, var(--warm-red), var(--warm-orange) 55%, #d9452f 100%);
  }

  .divider { position: absolute; left: 586px; top: 565px; width: 4px; height: 480px; background: var(--divider); }
  .divider-gap { position: absolute; left: 584px; top: 565px; width: 12px; height: 480px; background: #8a3b2c; }

  .wordmark {
    position: absolute; left: 0; right: 0; text-align: center;
    font-weight: 700; color: var(--ink); letter-spacing: 1px; white-space: nowrap;
  }
  .card-front .wordmark { top: 262px; font-size: 50px; }
  .card-back-art .wordmark { top: 222px; font-size: 33px; }

  .card-back-info { left: 596px; top: 565px; width: 392px; height: 480px; background: var(--paper); }

  .holder-name {
    position: absolute; left: 53px; top: 118px; font-size: 35px; font-weight: 700;
    color: var(--name-ink); letter-spacing: 0.5px;
    text-shadow: 1px 1px 0 var(--name-edge), -1px -1px 0 var(--name-edge), 1px -1px 0 var(--name-edge), -1px 1px 0 var(--name-edge);
  }
  .holder-position {
    position: absolute; left: 124px; top: 160px; font-size: 23px; font-style: italic; font-weight: 700; color: var(--position);
  }

  .contact-list { position: absolute; left: 40px; top: 245px; list-style: none; }
  .contact-item { display: flex; align-items: center; height: 38px; }
  .contact-icon { width: 61px; height: 38px; display: flex; align-items: center; justify-content: center; }
  .contact-icon.phone { background: var(--tile-phone); }
  .contact-icon.mail { background: var(--tile-mail); }
  .contact-icon.web { background: var(--tile-web); }
  .contact-text { margin-left: 22px; font-size: 18px; color: var(--ink); }
  .contact-text.phone-number { font-weight: 700; font-size: 19px; }
</style>
</head>
<body>
<div class="canvas">

  <section class="card-front">
    <div class="prism-field" role="img" aria-label="Faceted prism background in red, orange, yellow and dark tones"></div>
    <div class="wordmark">The Harbor Quill</div>
  </section>

  <section class="card-back-art">
    <div class="prism-field" role="img" aria-label="Faceted prism background in red, orange and yellow tones"></div>
    <div class="wordmark">The Harbor Quill</div>
  </section>

  <div class="divider-gap"></div>
  <div class="divider"></div>

  <section class="card-back-info">
    <div class="holder-name">YOURNAME</div>
    <div class="holder-position">Position</div>

    <ul class="contact-list">
      <li class="contact-item">
        <span class="contact-icon phone">
          <svg width="28" height="26" viewBox="0 0 28 26" aria-hidden="true">
            <path d="M3 9c0-4 5-6 11-6s11 2 11 6v2h-6V8c-3-1-7-1-10 0v3H3z" fill="#111"/>
            <path d="M7 12h14l3 11H4z" fill="#111"/>
            <circle cx="14" cy="17" r="3" fill="#7a2a22"/>
          </svg>
        </span>
        <span class="contact-text phone-number">000-000-000</span>
      </li>
      <li class="contact-item">
        <span class="contact-icon mail">
          <svg width="30" height="22" viewBox="0 0 30 22" aria-hidden="true">
            <rect x="1.5" y="1.5" width="27" height="19" fill="none" stroke="#111" stroke-width="2.5"/>
            <path d="M2 2l13 10L28 2M2 20l10-9M28 20l-10-9" fill="none" stroke="#111" stroke-width="2.5"/>
          </svg>
        </span>
        <span class="contact-text">your_email@mailbox.com</span>
      </li>
      <li class="contact-item">
        <span class="contact-icon web">
          <svg width="28" height="28" viewBox="0 0 28 28" aria-hidden="true">
            <circle cx="14" cy="14" r="12" fill="#111"/>
            <ellipse cx="14" cy="14" rx="5" ry="12" fill="none" stroke="#9dab5a" stroke-width="1.6"/>
            <path d="M2 14h24M4 8h20M4 20h20" stroke="#9dab5a" stroke-width="1.6"/>
          </svg>
        </span>
        <span class="contact-text">www.website.com</span>
      </li>
    </ul>
  </section>

</div>
</body>
</html>
```